RV38

We want a trendy packaging design for our mobile accessories. Initially we will be offering TPU cases to our retail customers and than we will introduce other similar accessories such as car chargers, AC chargers, data cables etc..
We would like to see designs that are unique, practical and appealing to the general audience.
Updates

Hi Everyone

There is guaranteed payment for the best designer of this packaging.

thanks

Reason: Hi All This will give you all more time to submit your designs :) regards

Target Market(s)

Telco retail store customers

Industry/Entity Type

Retail

Requirements
Must have
• Colorful , Fun , Sexy

```html
<!DOCTYPE html>
<html lang="en">
<head>
<meta charset="utf-8">
<title>RV38 TPU Cases – Packaging Dieline</title>
<link rel="stylesheet" href="https://fonts.googleapis.com/css2?family=Libre+Baskerville:wght@700&display=swap">
<style>
  :root {
    --page: #ffffff;
    --board-light: #f1f1f1;
    --board-mid: #e2e2e2;
    --board-dark: #cfcfcf;
    --fold: #fafafa;
    --slot: #8e8e8e;
    --navy: #141a5c;
    --wave-deep: #1b4fc4;
    --wave-mid: #1a8fe0;
    --wave-light: #6cc8f4;
    --wave-pale: #cfeefc;
  }
  html, body {
    margin: 0;
    padding: 0;
    width: 1200px;
    height: 1134px;
    overflow: hidden;
    background: var(--page);
  }
  .dieline {
    display: block;
    width: 1200px;
    height: 1134px;
  }
  .brand-name {
    font-family: "Libre Baskerville", Georgia, serif;
    font-weight: 700;
    fill: var(--navy);
  }
  .product-line {
    font-family: "Libre Baskerville", Georgia, serif;
    font-weight: 700;
    fill: var(--navy);
  }
  .panel { fill: url(#boardShade); }
  .fold-line { stroke: var(--fold); stroke-width: 2; fill: none; }
  .hang-slot { fill: var(--slot); }
  .window-cutout { fill: var(--page); stroke: var(--board-dark); stroke-width: 2; }
</style>
</head>
<body>
<svg class="dieline" viewBox="0 0 1200 1134" xmlns="http://www.w3.org/2000/svg">
  <defs>
    <linearGradient id="boardShade" x1="0" y1="0" x2="1" y2="1">
      <stop offset="0" stop-color="var(--board-light)"/>
      <stop offset="0.6" stop-color="var(--board-mid)"/>
      <stop offset="1" stop-color="var(--board-dark)"/>
    </linearGradient>
    <linearGradient id="waveBand" x1="0" y1="0" x2="1" y2="0.4">
      <stop offset="0" stop-color="var(--wave-pale)" stop-opacity="0.5"/>
      <stop offset="0.25" stop-color="var(--wave-mid)" stop-opacity="0.7"/>
      <stop offset="0.45" stop-color="var(--wave-deep)" stop-opacity="0.75"/>
      <stop offset="0.6" stop-color="var(--wave-light)" stop-opacity="0.6"/>
      <stop offset="0.8" stop-color="var(--wave-mid)" stop-opacity="0.85"/>
      <stop offset="1" stop-color="var(--wave-deep)" stop-opacity="0.8"/>
    </linearGradient>
    <linearGradient id="waveFade" x1="0" y1="0" x2="0" y2="1">
      <stop offset="0" stop-color="#fff" stop-opacity="0.85"/>
      <stop offset="0.3" stop-color="#fff" stop-opacity="0"/>
      <stop offset="0.8" stop-color="#fff" stop-opacity="0"/>
      <stop offset="1" stop-color="#fff" stop-opacity="0.75"/>
    </linearGradient>
  </defs>

  <!-- Box panels -->
  <g class="box-net">
    <rect class="panel hang-tab" x="82" y="76" width="336" height="151"/>
    <rect class="panel hang-tab-base" x="82" y="227" width="336" height="128"/>
    <rect class="panel side-top" x="418" y="227" width="182" height="128"/>
    <rect class="panel tuck-flap" x="600" y="124" width="333" height="58"/>
    <rect class="panel top-lid" x="600" y="182" width="333" height="173"/>
    <rect class="panel side-top" x="933" y="236" width="180" height="119"/>
    <rect class="panel body" x="82" y="355" width="1031" height="696"/>
  </g>

  <!-- Wave artwork band -->
  <g class="wave-artwork" role="img" aria-label="Flowing blue and grey abstract wave lines sweeping across the box sides">
    <rect x="82" y="355" width="1031" height="554" fill="url(#waveBand)"/>
    <rect x="82" y="355" width="1031" height="554" fill="url(#waveFade)"/>
  </g>

  <!-- Fold lines -->
  <g class="fold-lines">
    <line class="fold-line" x1="82" y1="227" x2="418" y2="227"/>
    <line class="fold-line" x1="82" y1="355" x2="1113" y2="355"/>
    <line class="fold-line" x1="82" y1="909" x2="1113" y2="909"/>
    <line class="fold-line" x1="600" y1="182" x2="933" y2="182"/>
    <line class="fold-line" x1="418" y1="227" x2="418" y2="1051"/>
    <line class="fold-line" x1="600" y1="124" x2="600" y2="1051"/>
    <line class="fold-line" x1="933" y1="236" x2="933" y2="1051"/>
  </g>

  <!-- Hang slots -->
  <g class="hang-slots">
    <rect class="hang-slot" x="182" y="172" width="118" height="28" rx="14"/>
    <rect class="hang-slot" x="182" y="242" width="118" height="30" rx="15"/>
  </g>

  <!-- Display window -->
  <rect class="window-cutout" x="658" y="404" width="211" height="369" rx="26"/>

  <!-- Front-left panel branding -->
  <text class="brand-name" x="140" y="448" font-size="50">RV38</text>
  <text class="product-line" x="140" y="484" font-size="20" letter-spacing="11">TPU cases</text>

  <!-- Narrow side, vertical -->
  <g transform="translate(488 410) rotate(90)">
    <text class="brand-name" x="0" y="0" font-size="40">RV38</text>
    <text class="product-line" x="128" y="-4" font-size="19" letter-spacing="2">TPU cases</text>
  </g>

  <!-- Top lid branding -->
  <text class="brand-name" x="766" y="282" font-size="52" text-anchor="middle">RV38</text>

  <!-- Window panel branding -->
  <text class="brand-name" x="768" y="830" font-size="52" text-anchor="middle">RV38</text>
  <text class="product-line" x="768" y="870" font-size="20" letter-spacing="11" text-anchor="middle">TPU cases</text>

  <!-- Right side, vertical -->
  <g transform="translate(1040 866) rotate(-90)">
    <text class="brand-name" x="0" y="0" font-size="34">RV38</text>
    <text class="product-line" x="108" y="-2" font-size="18" letter-spacing="2">TPU cases</text>
  </g>
</svg>
</body>
</html>
```